Home Design company focused on remodel and enhancement of kitchens and bathroorms

I already have a logo designed by ArtHarbor, I now need a design for my business cards.
The company is in the remodeling and enhancement industry for homes, focusing on kitchens and bathrooms, however, we can remodel or enhance every room in a home, an office space, etc.

The company's name is VELMOR HOME DESIGN, LLC

We'll focus on clients in the Rio Grande Valley, Texas. Primarily McAllen, Edinburg, Pharr, Mission, Brownsville and South Padre Island.

The design on the business card should transmit reliability, professionalism anda bit of upscale design.

The logo is in black and white, and would like to keep it that way.

The information that needs to be printed in the business cards is:
Company's name: Velmor Home Design
Company's Logo (attached)
My name: Noel Bramwit
Address, phone and email:
2715 N Parkline Road, Ste 348
Brinmoor, OR 97412
(555) 555 0187
nbramwit@velmordesign.example
Website: velmordesign.example

```html
<!DOCTYPE html>
<html lang="en">
<head>
<meta charset="utf-8">
<title>Velmor Home Design — Business Card</title>
<link href="https://fonts.googleapis.com/css2?family=Lato:wght@400;700&display=swap" rel="stylesheet">
<style>
  :root {
    --backdrop: #e4e4e4;
    --card: #ffffff;
    --ink: #111111;
    --ink-soft: #333333;
  }
  * { margin: 0; padding: 0; box-sizing: border-box; }
  html, body {
    width: 1200px;
    height: 801px;
    overflow: hidden;
    background: var(--backdrop);
    font-family: "Lato", sans-serif;
    color: var(--ink);
  }
  .canvas {
    position: relative;
    width: 1200px;
    height: 801px;
  }
  .card {
    position: absolute;
    left: 351px;
    width: 529px;
    height: 302px;
    background: var(--card);
  }
  .card--front { top: 43px; }
  .card--back  { top: 419px; }

  .holder-name {
    position: absolute;
    left: 33px;
    top: 121px;
    font-size: 23px;
    font-weight: 400;
    letter-spacing: 0.2px;
    text-transform: uppercase;
  }
  .name-rule {
    position: absolute;
    left: 33px;
    top: 160px;
    width: 25px;
    height: 2px;
    background: var(--ink);
  }
  .company-name {
    position: absolute;
    left: 33px;
    top: 170px;
    font-size: 11px;
    font-weight: 700;
    letter-spacing: 1.1px;
    text-transform: uppercase;
  }
  .company-address {
    position: absolute;
    left: 33px;
    top: 189px;
    font-size: 8.5px;
    letter-spacing: 0.5px;
    color: var(--ink-soft);
  }
  .contact-list {
    position: absolute;
    left: 33px;
    top: 227px;
    list-style: none;
    font-size: 11px;
    line-height: 15.5px;
    color: var(--ink-soft);
  }
  .contact-label { font-weight: 700; color: var(--ink); margin-right: 4px; }

  .brand {
    position: absolute;
    left: 50%;
    top: 50%;
    transform: translate(-50%, -50%);
    display: flex;
    align-items: center;
    gap: 10px;
    white-space: nowrap;
  }
  .brand-square {
    width: 12px;
    height: 12px;
    background: var(--ink);
  }
  .brand-name {
    font-size: 15px;
    font-weight: 400;
    letter-spacing: 3px;
    text-transform: uppercase;
    color: var(--ink);
  }
</style>
</head>
<body>
  <main class="canvas">
    <section class="card card--front" aria-label="Business card front">
      <h1 class="holder-name">Noel Bramwit</h1>
      <div class="name-rule"></div>
      <p class="company-name">Velmor Home Design</p>
      <p class="company-address">2715 N Parkline Road, Ste 348, Brinmoor, OR 97412</p>
      <ul class="contact-list">
        <li><span class="contact-label">e.</span>nbramwit@velmordesign.example</li>
        <li><span class="contact-label">w.</span>www.velmordesign.example</li>
        <li><span class="contact-label">t.</span>(555) 555 0187</li>
      </ul>
    </section>

    <section class="card card--back" aria-label="Business card back">
      <div class="brand">
        <span class="brand-square"></span>
        <span class="brand-name">Velmor Home Design</span>
      </div>
    </section>
  </main>
</body>
</html>
```